Brindle Offers is an online marketing platform.

A daily deals site for consumers a way to bring in new clients for clients and this is who the business cards are for. Industries - Food and Drink, Things To Do, Beauty and Spas, Staycations and Services.
Logo on one side.
Name - Owen Radley
Job Title - Sales Director
Phone Number - 07912358046
Email - owen@brindleoffers.co.uk
need same for second person
Name - Fiona Bracken
Job Title - Operations Director
Phone Number - 01632840275
Email - fiona@brindleoffers.co.uk
Bottom Right - Chatterbook Icon, Snapa Icon, Pipline Icon
Target Market(s)
Business owners of the above industries
Contact Information for Business Card
Name - Owen Radley
Name - Fiona Bracken
Look and feel

```html
<!DOCTYPE html>
<html lang="en">
<head>
<meta charset="utf-8">
<title>Brindle Offers – Business Cards</title>
<link rel="stylesheet" href="https://fonts.googleapis.com/css2?family=Montserrat:wght@300;400;600;800&display=swap">
<style>
  :root {
    --stage: #262626;
    --card-dark: #0b0b0b;
    --card-dark-tone: #1c1c1c;
    --card-light: #c9c9c9;
    --card-light-tone: #b9b9b9;
    --ink: #111111;
    --paper: #ffffff;
    --frame-grey: #555555;
    --line-white: #f4f4f4;
  }
  * { box-sizing: border-box; margin: 0; padding: 0; }
  html, body {
    width: 1200px; height: 900px; overflow: hidden;
    background: var(--stage);
    font-family: "Montserrat", sans-serif;
  }
  .stage {
    width: 1200px; height: 900px;
    display: flex; flex-direction: column; align-items: center; justify-content: center; gap: 40px;
  }
  .stage__row { display: flex; gap: 40px; }
  .card {
    position: relative;
    width: 560px; height: 320px;
    border-radius: 22px;
    overflow: hidden;
    flex: none;
  }
  .card__pattern { position: absolute; inset: 0; }

  /* Front: logo side */
  .card--front { background: var(--card-dark); }
  .card--front .card__pattern {
    background: linear-gradient(135deg, var(--card-dark-tone), var(--card-dark) 55%, var(--card-dark-tone));
  }
  .front__lines { position: absolute; inset: 0; }
  .logo-box {
    position: absolute; left: 50%; top: 50%;
    width: 170px; height: 160px;
    transform: translate(-50%, -50%);
    background: var(--card-dark);
    border: 2px solid var(--line-white);
    display: flex; flex-direction: column; align-items: center; justify-content: center;
    color: var(--line-white);
    font-weight: 300;
    text-transform: uppercase;
    letter-spacing: 0.26em;
    font-size: 15px; line-height: 1.6;
    text-align: center;
  }
  .logo-box__mark {
    width: 26px; height: 26px;
    border: 2px solid var(--line-white);
    margin-bottom: 14px;
  }

  /* Back: contact side */
  .card--back { background: var(--card-light); color: var(--ink); }
  .card--back .card__pattern {
    background: linear-gradient(135deg, var(--card-light), var(--card-light-tone) 50%, var(--card-light));
  }
  .name-box {
    position: absolute; left: 170px; top: 40px;
    width: 230px; height: 165px;
    background: var(--paper);
    border: 4px solid var(--frame-grey);
    display: flex; flex-direction: column; justify-content: flex-end;
    padding: 0 14px 16px;
  }
  .name-box__name {
    font-weight: 800; font-size: 18px; text-transform: uppercase; line-height: 1.1;
    white-space: nowrap;
  }
  .name-box__title {
    font-weight: 400; font-size: 13px; text-transform: uppercase; line-height: 1.3;
    white-space: nowrap;
  }
  .socials {
    position: absolute; right: 20px; top: 228px;
    display: flex; gap: 12px;
    font-size: 9px; font-weight: 600; text-transform: uppercase; letter-spacing: 0.02em;
  }
  .socials span { display: flex; align-items: center; gap: 4px; }
  .socials span::before {
    content: ""; width: 7px; height: 7px; border: 1.5px solid var(--ink); border-radius: 2px;
  }
  .contact-row {
    position: absolute; left: 20px; bottom: 18px;
    display: flex; align-items: center; gap: 28px;
    font-size: 11.5px; font-weight: 400; text-transform: uppercase; letter-spacing: 0.04em;
    white-space: nowrap;
  }
  .contact-item { display: flex; align-items: center; gap: 6px; }
  .contact-item svg { width: 12px; height: 12px; fill: var(--ink); flex: none; }
</style>
</head>
<body>
<main class="stage">

  <div class="stage__row">
    <section class="card card--front">
      <div class="card__pattern" role="img" aria-label="Dark geometric triangle pattern background"></div>
      <svg class="front__lines" viewBox="0 0 560 320" aria-hidden="true">
        <g fill="none" stroke="var(--line-white)" stroke-width="2.5">
          <rect x="150" y="50" width="260" height="220"/>
          <line x1="40" y1="0" x2="40" y2="320"/>
          <line x1="520" y1="0" x2="520" y2="320"/>
        </g>
      </svg>
      <div class="logo-box">
        <span class="logo-box__mark" aria-hidden="true"></span>
        <span>Brindle</span>
        <span>Offers</span>
      </div>
    </section>
  </div>

  <div class="stage__row">
    <section class="card card--back">
      <div class="card__pattern" role="img" aria-label="Light grey geometric triangle pattern background"></div>
      <div class="name-box">
        <p class="name-box__name">Owen Radley</p>
        <p class="name-box__title">Sales Director</p>
      </div>
      <p class="socials">
        <span>Chatterbook</span>
        <span>Pipline</span>
        <span>Snapa</span>
      </p>
      <div class="contact-row">
        <p class="contact-item">
          <svg viewBox="0 0 12 12" aria-hidden="true"><path d="M0 2h12v8H0z M0 2l6 5 6-5" stroke="#c9c9c9" stroke-width="1"/></svg>
          owen@brindleoffers.co.uk
        </p>
        <p class="contact-item">
          <svg viewBox="0 0 12 12" aria-hidden="true"><path d="M2 0l3 3-1.5 2a7 7 0 0 0 3.5 3.5L9 7l3 3-2 2C5 12 0 7 0 2z"/></svg>
          07912358046
        </p>
      </div>
    </section>

    <section class="card card--back">
      <div class="card__pattern" role="img" aria-label="Light grey geometric triangle pattern background"></div>
      <div class="name-box">
        <p class="name-box__name">Fiona Bracken</p>
        <p class="name-box__title">Operations Director</p>
      </div>
      <p class="socials">
        <span>Chatterbook</span>
        <span>Pipline</span>
        <span>Snapa</span>
      </p>
      <div class="contact-row">
        <p class="contact-item">
          <svg viewBox="0 0 12 12" aria-hidden="true"><path d="M0 2h12v8H0z M0 2l6 5 6-5" stroke="#c9c9c9" stroke-width="1"/></svg>
          fiona@brindleoffers.co.uk
        </p>
        <p class="contact-item">
          <svg viewBox="0 0 12 12" aria-hidden="true"><path d="M2 0l3 3-1.5 2a7 7 0 0 0 3.5 3.5L9 7l3 3-2 2C5 12 0 7 0 2z"/></svg>
          01632840275
        </p>
      </div>
    </section>
  </div>

</main>
</body>
</html>
```